Tamarack Hearth Partners Business Card

Looking for a new business card layout. We are a real estate firm w/ a logo, old design attached. Must keep the same elements on there, just need a fresh look and possible some foil accents. Looking for a simpler design w/ more modern style.

Target Market(s)

Real Estate clients

Industry/Entity Type

Real Estate Agent

Contact Information for Business Card

see attached

Font styles to use
Sans Serif

Requirements
Must have
• all elements on current biz card
Nice to have
• modern look, simpler than we have!
Should not have
• no serif fonts

```html
<!DOCTYPE html>
<html lang="en">
<head>
<meta charset="utf-8">
<title>Tamarack Hearth Partners Business Card</title>
<link href="https://fonts.googleapis.com/css2?family=Roboto:wght@400;500;700;900&display=swap" rel="stylesheet">
<style>
  :root {
    --backdrop: #2f2f2f;
    --card: #ffffff;
    --ink: #1a1a1a;
    --text: #3a3a3a;
    --brand-blue: #27a9e1;
    --brand-green: #8dc63f;
    --photo-light: #eee8de;
    --photo-hair: #d8c3a0;
    --photo-top: #3fc9bd;
  }
  * { box-sizing: border-box; margin: 0; padding: 0; }
  html, body { width: 1200px; height: 1200px; overflow: hidden; }
  body {
    background: var(--backdrop);
    font-family: "Roboto", Arial, sans-serif;
    display: flex;
    flex-direction: column;
    align-items: center;
    justify-content: center;
    gap: 44px;
  }
  .card {
    width: 900px;
    height: 514px;
    background: var(--card);
    position: relative;
    overflow: hidden;
  }

  /* Back side */
  .card--back {
    display: flex;
    flex-direction: column;
    align-items: center;
    justify-content: center;
  }
  .brand {
    display: flex;
    align-items: center;
    gap: 14px;
    font-weight: 900;
    color: var(--ink);
    line-height: 1.05;
  }
  .brand__mark {
    width: 18px; height: 18px;
    background: var(--brand-green);
    flex: none;
  }
  .card--back .brand { font-size: 52px; }
  .card--back .brand__mark { width: 26px; height: 26px; }
  .back__web {
    position: absolute;
    bottom: 56px;
    left: 0; right: 0;
    text-align: center;
    font-size: 22px;
    color: var(--text);
  }

  /* Front side */
  .front__info {
    position: absolute;
    left: 60px;
    top: 58px;
    width: 420px;
    z-index: 2;
  }
  .card--front .brand { font-size: 34px; width: 300px; align-items: flex-start; }
  .card--front .brand__mark { margin-top: 8px; }
  .agent__name {
    margin-top: 30px;
    font-size: 34px;
    font-weight: 700;
    color: var(--brand-blue);
  }
  .agent__title {
    font-size: 24px;
    color: var(--brand-green);
    margin-top: 2px;
  }
  .agent__address {
    margin-top: 20px;
    font-size: 22px;
    line-height: 1.3;
    color: var(--text);
    font-style: normal;
  }
  .contact {
    list-style: none;
    margin-top: 16px;
    font-size: 22px;
    color: var(--text);
  }
  .contact li {
    display: flex;
    align-items: center;
    gap: 8px;
    line-height: 1.35;
  }
  .contact svg { width: 18px; height: 18px; flex: none; }
  .front__photo {
    position: absolute;
    right: 0; top: 0;
    width: 560px; height: 100%;
    background:
      linear-gradient(to right, var(--card) 0%, rgba(255,255,255,0) 40%),
      linear-gradient(to bottom, var(--photo-light) 0%, var(--photo-hair) 48%, #e9c6b0 62%, var(--photo-top) 100%);
  }
</style>
</head>
<body>

  <section class="card card--back">
    <div class="brand"><span class="brand__mark"></span><span>Tamarack Hearth Partners</span></div>
    <p class="back__web">TamarackHearth-Homes.com</p>
  </section>

  <section class="card card--front">
    <div class="front__info">
      <div class="brand"><span class="brand__mark"></span><span>Tamarack Hearth Partners</span></div>
      <h1 class="agent__name">Dana Whitfield</h1>
      <p class="agent__title">Principal Broker</p>
      <address class="agent__address">482 NW Birch Ave.<br>Pinecrest, OR 97700</address>
      <ul class="contact">
        <li>
          <svg viewBox="0 0 24 24"><path fill="#27a9e1" d="M6.6 10.8a15 15 0 0 0 6.6 6.6l2.2-2.2c.3-.3.7-.4 1-.2 1.1.4 2.3.6 3.6.6.6 0 1 .4 1 1V20c0 .6-.4 1-1 1A17 17 0 0 1 3 4c0-.6.4-1 1-1h3.5c.6 0 1 .4 1 1 0 1.3.2 2.5.6 3.6.1.3 0 .7-.2 1z"/></svg>
          541.555.0142
        </li>
        <li>
          <svg viewBox="0 0 24 24"><rect x="6" y="2" width="12" height="20" rx="2" fill="none" stroke="#27a9e1" stroke-width="2"/><circle cx="12" cy="18" r="1.2" fill="#27a9e1"/></svg>
          541-555-0187
        </li>
        <li>
          <svg viewBox="0 0 24 24"><rect x="2" y="5" width="20" height="14" rx="1.5" fill="#27a9e1"/><path d="M3 6l9 7 9-7" fill="none" stroke="#fff" stroke-width="1.6"/></svg>
          dana@tamarackhearth.com
        </li>
        <li>
          <svg viewBox="0 0 24 24"><g fill="none" stroke="#27a9e1" stroke-width="1.6"><circle cx="12" cy="12" r="9"/><ellipse cx="12" cy="12" rx="4" ry="9"/><path d="M3 12h18M5 7h14M5 17h14"/></g></svg>
          TamarackHearth-Homes.com
        </li>
      </ul>
    </div>
    <div class="front__photo" role="img" aria-label="Portrait photo of the broker, smiling, in a turquoise top, fading softly into the white card"></div>
  </section>

</body>
</html>
```